Redesign two existing website pages and one new landing page for dental office

I need to redesign two webpages on my dental website, the Home page (http://brelvoortdental.com) and the Dental Implant Services page (http://www.brelvoortdental.com/dental-implant-services) and also create a landing page for the Dental Implant Services page.

Please use the same color scheme, slogans and subtitles for the redesign pages and create a reserved video spot on each page. The video spots should not be too big but not too small either and positioned in a central key location on each of the pages. The final redesigned pages should communicate leadership, confidence and trust.

The new landing page for the Dental implant Services page must not have any hyperlinks on the page and must entice the viewer to give name and email before downloading a "Free" eBook called "Is a Fresh Smile Worth Waiting For?" Any added photo images to this new page must be smiling.
Updates

Project Deadline Extended Reason: I got feedback that my project was not long enough so I'm extending it by 5 days. Added Thursday, April 16, 2015

Target Market(s)

People who are middle-age to seniors.

Industry/Entity Type

Dental

Coding

Coded - Design and coding required

Number of Pages Required

3 page

Requirements
Must have
• Compatible with existing website colors and theme.

```html
<!DOCTYPE html>
<html lang="en">
<head>
<meta charset="utf-8">
<title>Brelvoort Dental Care – Home</title>
<link href="https://fonts.googleapis.com/css2?family=Open+Sans:wght@400;600;700&family=Oswald:wght@400;500&display=swap" rel="stylesheet">
<style>
:root{
  --green-dark:#2d4a40;
  --green:#3b6b58;
  --green-accent:#5f9c6e;
  --ink:#333b38;
  --muted:#7a807d;
  --line:#dfe3e1;
  --card:#eef1ef;
  --hero-a:#e7e9e8;
  --hero-b:#b9bebc;
  --footer:#2b3c35;
  --footer-deep:#1f2c27;
  --white:#ffffff;
}
*{box-sizing:border-box;margin:0;padding:0}
html,body{width:669px;height:1200px;overflow:hidden}
body{font-family:"Open Sans",Arial,sans-serif;color:var(--ink);background:var(--white);font-size:9px;line-height:1.45}

.topbar{height:18px;background:var(--footer-deep);color:#c9d1cd;font-size:7px;display:flex;align-items:center;padding:0 40px}
.topbar span{margin-right:18px}

.header{height:60px;display:flex;align-items:center;justify-content:space-between;padding:0 40px;border-bottom:1px solid var(--line)}
.brand{display:flex;align-items:center;gap:7px;font-size:17px;font-weight:700;color:var(--green)}
.brand i{width:12px;height:12px;border-radius:50%;background:var(--green-accent);display:block}
.header-right{display:flex;flex-direction:column;align-items:flex-end;gap:6px}
.callbar{display:flex;align-items:center;gap:4px;font-size:7px;color:var(--muted)}
.callbar b{color:var(--green);margin-right:6px}
.callbar em{width:9px;height:9px;background:var(--green);display:block}
.nav{display:flex;font-size:7.5px;font-weight:600}
.nav a{padding:7px 8px;color:var(--ink);text-decoration:none}
.nav a.active{background:var(--green);color:var(--white)}

.hero{height:307px;position:relative;background:linear-gradient(90deg,var(--hero-a),#d4d7d6 55%,var(--hero-b))}
.hero-photo{position:absolute;right:0;top:0;width:380px;height:100%;background:linear-gradient(160deg,#ece7e2,#c9bcb2 55%,#9fa6a3)}
.hero-copy{position:absolute;left:48px;top:128px}
.hero-copy h1{font-size:20px;font-weight:600;line-height:1.3;color:var(--ink)}
.hero-copy h1 strong{color:var(--green);font-weight:700}
.btn{display:inline-block;background:var(--footer);color:var(--white);font-size:7.5px;font-weight:700;padding:8px 14px;letter-spacing:.3px}
.hero-copy .btn{margin-top:16px}
.dots{position:absolute;left:70px;bottom:24px;display:flex;gap:4px}
.dots i{width:5px;height:5px;border-radius:50%;background:#8d9390;display:block}
.dots i:first-child{background:var(--ink)}

.features{display:flex;gap:18px;padding:28px 40px 0;height:237px}
.feature{flex:1}
.feature h3{font-size:9.5px;font-weight:600;text-transform:uppercase;border-bottom:1px solid var(--line);padding-bottom:5px;margin-bottom:7px}
.feature .pic{height:82px;margin-bottom:8px;position:relative}
.feature h4{font-size:8px;font-weight:700;margin-bottom:3px}
.feature p{font-size:6.5px;color:var(--muted)}
.feature .more{font-size:6.5px;font-weight:700;margin-top:5px;display:block}
.pic-hygiene{background:linear-gradient(135deg,#f1ebe6,#d8c8bc)}
.pic-emergency{background:linear-gradient(135deg,#e9dfd7,#c7ab98)}
.pic-video{background:linear-gradient(135deg,#d9e2e4,#9fb3b8)}
.play{position:absolute;left:50%;top:50%;transform:translate(-50%,-50%)}

.cta-band{height:48px;background:var(--green);display:flex;align-items:center;justify-content:center;gap:22px}
.cta-band p{color:var(--white);font-size:11px;font-weight:600}
.cta-band .btn{background:var(--white);color:var(--green)}

.services{padding:28px 40px 0;height:350px;text-align:center}
.services h2{font-family:"Oswald",sans-serif;font-size:22px;font-weight:400;letter-spacing:.5px;color:var(--ink)}
.services h2 span{color:var(--green-accent)}
.services .lead{font-size:6.5px;color:var(--muted);width:460px;margin:6px auto 16px}
.cards{display:flex;gap:6px}
.card{flex:1;background:var(--card);height:194px;padding:18px 12px 0}
.card .avatar{width:46px;height:46px;border-radius:50%;margin:0 auto 14px;border:2px solid var(--white)}
.av-dentures{background:radial-gradient(circle,#e8d6c8,#b99a86)}
.av-cosmetic{background:radial-gradient(circle,#efe0d4,#c7a690)}
.av-implant{background:radial-gradient(circle,#e4cfc0,#a78470)}
.av-sedation{background:radial-gradient(circle,#e6e6dc,#b3b8a8)}
.card h4{font-size:9px;font-weight:700;margin-bottom:6px}
.card ul{list-style:none;font-size:6.5px;color:var(--muted);text-align:left;padding-left:8px}

.footer{height:200px;background:var(--footer);color:#cfd8d3;display:flex;gap:20px;padding:20px 40px 0}
.footer h5{font-size:9px;font-weight:700;color:var(--white);text-transform:uppercase;margin-bottom:10px}
.footer p,.footer li{font-size:6.5px}
.col-wait{width:170px}
.wait-body{display:flex;gap:8px}
.wait-pic{width:44px;height:52px;flex:none;background:linear-gradient(135deg,#e2d3c6,#a88e7b)}
.col-blog{width:175px}
.post{display:flex;gap:8px;margin-bottom:8px}
.date{width:28px;height:30px;flex:none;background:var(--green-accent);color:var(--white);text-align:center;font-weight:700;font-size:11px;line-height:1.1;padding-top:3px}
.date small{display:block;font-size:5.5px;font-weight:600}
.col-contact{flex:1}
.map{height:62px;background:linear-gradient(135deg,#e3e6dc,#c6ccbe);margin-bottom:8px}
.footer dl{display:grid;grid-template-columns:38px 1fr;font-size:6.5px;row-gap:2px}
.footer dt{color:var(--white);font-weight:600}

.copyright{height:20px;background:var(--footer-deep);color:#8c9892;font-size:6px;display:flex;align-items:center;justify-content:center}
</style>
</head>
<body>

<div class="topbar"><span>Text Us Anytime Available Here</span><span>Flexible Payment Options</span></div>

<header class="header">
  <div class="brand"><i></i>Brelvoort Dental Care</div>
  <div class="header-right">
    <div class="callbar">Call Us Today | <b>(555) 214-0187</b><em></em><em></em><em></em><em></em></div>
    <nav class="nav">
      <a class="active" href="#">HOME</a><a href="#">ABOUT US</a><a href="#">DENTAL SERVICES</a><a href="#">BLOG</a><a href="#">CONTACT US</a><a href="#">TESTIMONIALS</a>
    </nav>
  </div>
</header>

<section class="hero">
  <div class="hero-photo" role="img" aria-label="Smiling multi-generation family posing together"></div>
  <div class="hero-copy">
    <h1>Life-Changing Family<br><strong>Dental Care In Cedar Hollow</strong></h1>
    <span class="btn">REQUEST AN APPOINTMENT</span>
  </div>
  <div class="dots"><i></i><i></i><i></i><i></i></div>
</section>

<section class="features">
  <article class="feature">
    <h3>Dental Hygiene Services</h3>
    <div class="pic pic-hygiene" role="img" aria-label="Patient smiling during a dental cleaning"></div>
    <h4>Achieve Better Health With Prevention</h4>
    <p>Regular cleanings keep your teeth and gums healthy and help you avoid costly problems later.</p>
    <span class="more">Read More ›</span>
  </article>
  <article class="feature">
    <h3>Dental Emergency Services</h3>
    <div class="pic pic-emergency" role="img" aria-label="Woman holding her cheek with tooth pain"></div>
    <h4>Stop Pain From Tooth Trauma &amp; Infection</h4>
    <p>Same-day visits are available for broken teeth, swelling and sudden pain when you need us most.</p>
    <span class="more">Read More ›</span>
  </article>
  <article class="feature">
    <h3>Welcome To Our Practice</h3>
    <div class="pic pic-video" role="img" aria-label="Video still of the dentist with a patient">
      <svg class="play" width="26" height="26" viewBox="0 0 26 26"><circle cx="13" cy="13" r="12" fill="#ffffff" opacity=".85"/><path d="M10 8l9 5-9 5z" fill="#3b6b58"/></svg>
    </div>
  </article>
</section>

<section class="cta-band">
  <p>Comprehensive Family Dentistry in One Cedar Hollow Dental Office!</p>
  <span class="btn">Schedule An Appointment</span>
</section>

<section class="services">
  <h2><span>OUR</span> SERVICES</h2>
  <p class="lead">We offer a full range of care for every age, from routine checkups to restorative treatment, all delivered with comfort and respect in one friendly office close to home.</p>
  <div class="cards">
    <div class="card">
      <div class="avatar av-dentures" role="img" aria-label="Smiling senior woman"></div>
      <h4>Beautiful Dentures</h4>
      <ul><li>What is a Denture?</li><li>Who Needs a Denture?</li><li>How Are Dentures Made?</li></ul>
    </div>
    <div class="card">
      <div class="avatar av-cosmetic" role="img" aria-label="Smiling young woman"></div>
      <h4>Cosmetic Dentistry</h4>
      <ul><li>Whiten Your Teeth</li><li>Porcelain Veneers</li><li>Clear Aligner Therapy</li></ul>
    </div>
    <div class="card">
      <div class="avatar av-implant" role="img" aria-label="Smiling woman with new implants"></div>
      <h4>Dental Implant Services</h4>
      <ul><li>Anchorage to the Jaw Bone</li><li>Replace 1 or More Missing Teeth</li><li>Stabilize Loose Dentures</li></ul>
    </div>
    <div class="card">
      <div class="avatar av-sedation" role="img" aria-label="Relaxed patient smiling"></div>
      <h4>Sedation Dentistry</h4>
      <ul><li>Control Dental Fear</li><li>Dental Pain Management</li><li>Relaxed and Tranquil Treatment</li></ul>
    </div>
  </div>
</section>

<footer class="footer">
  <div class="col-wait">
    <h5>Don't Wait 'Til It Hurts!</h5>
    <div class="wait-body">
      <div class="wait-pic" role="img" aria-label="Smiling patient portrait"></div>
      <p>Small problems grow quietly. A quick visit today can save your smile and spare you pain and expense tomorrow.</p>
    </div>
  </div>
  <div class="col-blog">
    <h5>Recent Blog Posts</h5>
    <div class="post"><div class="date">15<small>April</small></div><p>Simple habits that protect your gums at every age.</p></div>
    <div class="post"><div class="date">15<small>April</small></div><p>What to expect at your first implant consultation.</p></div>
    <div class="post"><div class="date">15<small>April</small></div><p>How sedation helps nervous patients feel calm.</p></div>
  </div>
  <div class="col-contact">
    <h5>Contact Us</h5>
    <div class="map" role="img" aria-label="Map showing the office location"></div>
    <dl>
      <dt>Address</dt><dd>4820 Linden Crest Rd, Cedar Hollow, TX 77000</dd>
      <dt>Email</dt><dd>hello@brelvoortdental.com</dd>
      <dt>Phone</dt><dd>(555) 214-0187</dd>
    </dl>
  </div>
</footer>

<div class="copyright">Copyright © 2015 Brelvoort Dental Care. All rights reserved.</div>

</body>
</html>
```